exclusive Speakeasy Bar Web design in New Jersey USA

We are opening a speakeasy in New Jersey USA soon. we are looking for a web designer to do our web site including the coding. we a looking for a 4 to 5 page web design. the site will be mostly static. home page, contact page, menu page and a link to a 3rd party site (most likely Qelmo) for reservations. we are looking for this designer to do our menu deign as well. we are looking for a quick turnaround 7-10 days. i am attaching some pictures for the designers to see the concept design and the actual current pictures with our logo as well. professionally taken pictures will be provided later on. our photographer will be taking the pictures in the next week.

Industry/Entity Type

Restaurant, Bar, Speakeasy

Coding

Coded - Design and coding required

Number of Pages Required

4 page

Requirements
Must have
• home page, contact page, menu page and a link to qelmo.com for reservations
Nice to have
• some videos

```html
<!DOCTYPE html>
<html lang="en">
<head>
<meta charset="utf-8">
<title>Velvet Key — Speakeasy, New Jersey</title>
<link href="https://fonts.googleapis.com/css2?family=Cinzel:wght@400;500;600&family=Righteous&family=Trirong:wght@400;600&display=swap" rel="stylesheet">
<style>
:root{
  --gold:#c79a4a;
  --gold-light:#d8b06a;
  --brown:#8a5c22;
  --brown-dark:#3a2710;
  --ink:#2b2b2b;
  --footer:#2a2724;
  --white:#ffffff;
}
*{margin:0;padding:0;box-sizing:border-box}
html,body{width:1200px;height:3229px;overflow:hidden}
body{position:relative;background:var(--white);font-family:"Trirong",serif;color:var(--ink)}
.abs{position:absolute}
a{color:inherit;text-decoration:none}

/* header */
.site-header{left:0;top:0;width:1200px;height:88px;background:var(--white);z-index:3}
.brand-box{left:88px;top:0;width:133px;height:163px;background:var(--white);z-index:4;display:flex;align-items:center;justify-content:center}
.brand-frame{width:105px;height:135px;border:2px solid var(--brown);display:flex;align-items:center;justify-content:center;text-align:center}
.brand-name{font-family:"Cinzel",serif;font-weight:600;font-size:19px;line-height:1.15;color:var(--ink);letter-spacing:1px}
.nav{top:33px;font-family:"Cinzel",serif;font-size:15px;letter-spacing:.5px;color:#222}
.nav .active{color:var(--gold);border-bottom:1px solid var(--gold)}
.btn{display:flex;align-items:center;justify-content:center;font-family:"Cinzel",serif;letter-spacing:.5px}
.book-btn{left:973px;top:22px;width:139px;height:43px;background:var(--brown);color:var(--white);font-size:15px}

/* hero */
.hero{left:0;top:88px;width:1200px;height:512px;background:linear-gradient(180deg,#2a2a26 0%,#3a3026 55%,#6b4d28 80%,#4a3622 100%)}
.hero-title{left:0;top:248px;width:1200px;text-align:center;font-family:"Righteous",sans-serif;font-size:50px;line-height:64px;letter-spacing:4px;color:var(--gold-light)}

/* about */
.section-title{font-family:"Cinzel",serif;font-weight:500;color:var(--brown);font-size:42px;letter-spacing:1px}
.title-rule{height:2px;width:54px;background:var(--gold)}
.about-title{left:88px;top:726px}
.about-rule{left:166px;top:774px}
.about-copy{left:88px;top:810px;width:425px;font-size:16px;line-height:24px;color:#333}
.about-copy p+p{margin-top:24px}
.read-btn{left:88px;top:1068px;width:139px;height:43px;background:var(--gold);color:var(--brown-dark);font-size:14px}
.photo-chef{left:848px;top:704px;width:264px;height:366px;background:linear-gradient(160deg,#1a1a1a 0%,#3b3632 50%,#d8d4cf 100%)}
.photo-wrap{left:608px;top:784px;width:320px;height:366px;background:var(--white)}
.photo-burrito{left:616px;top:792px;width:304px;height:350px;background:linear-gradient(150deg,#b23a2a 0%,#6a8a3a 35%,#d9d2b4 65%,#3a4a2a 100%)}

/* menu */
.menu-band{left:0;top:1247px;width:1200px;height:743px;background:linear-gradient(180deg,#3a2a16 0%,#4a3018 50%,#3c2710 100%)}
.menu-title{left:0;top:1336px;width:1200px;text-align:center;color:var(--gold)}
.menu-rule{left:573px;top:1386px}
.menu-card{top:1434px;width:319px;height:307px}
.card-food{left:88px;background:linear-gradient(160deg,#d9c8b0 0%,#8a4a1e 50%,#c03028 100%)}
.card-drinks{left:441px;background:linear-gradient(180deg,#151515 0%,#2a2420 60%,#3a2c20 100%);display:flex;justify-content:center;padding-top:78px}
.card-snacks{left:793px;background:linear-gradient(160deg,#2a2018 0%,#caa060 55%,#e7e2da 100%)}
.drinks-mark{width:90px;height:115px;border:2px solid var(--brown);color:var(--gold);font-family:"Cinzel",serif;font-size:15px;text-align:center;display:flex;align-items:center;justify-content:center;line-height:1.2}
.card-label{width:272px;height:63px;background:var(--white);color:var(--brown);font-family:"Cinzel",serif;font-size:20px;letter-spacing:.5px;display:flex;align-items:center;justify-content:center}

/* video */
.video-frame{left:176px;top:1871px;width:849px;height:458px;background:var(--white)}
.video{left:184px;top:1879px;width:832px;height:441px;background:linear-gradient(120deg,#1c1a18 0%,#2e2a26 55%,#4a4036 100%)}
.play{left:552px;top:2051px;width:96px;height:96px;border-radius:50%;background:rgba(199,154,74,.55);display:flex;align-items:center;justify-content:center}
.play-inner{width:68px;height:68px;border-radius:50%;background:#c89a55;display:flex;align-items:center;justify-content:center}

/* locate */
.locate-title{left:88px;top:2422px}
.locate-rule{left:160px;top:2470px}
.map{left:88px;top:2497px;width:672px;height:304px;background:linear-gradient(135deg,#e8e4dc 0%,#f1ede3 45%,#a9c6ee 75%,#e8e4dc 100%)}
.contact-item{left:816px;width:320px;height:52px}
.contact-icon{position:absolute;left:0;top:0;width:52px;height:52px;background:var(--brown);display:flex;align-items:center;justify-content:center}
.contact-text{position:absolute;left:67px;top:2px}
.contact-label{font-family:"Cinzel",serif;color:var(--brown);font-size:14px}
.contact-value{font-weight:600;font-size:16px;color:#222;letter-spacing:.5px}

/* footer */
.site-footer{left:0;top:2913px;width:1200px;height:316px;background:var(--footer)}
.footer-brand{left:88px;top:2970px;width:119px;height:155px;border:2px solid var(--brown);display:flex;align-items:center;justify-content:center;text-align:center;font-family:"Cinzel",serif;font-size:20px;color:var(--gold);line-height:1.2}
.footer-head{font-family:"Cinzel",serif;color:var(--gold);font-size:17px;letter-spacing:.5px}
.footer-rule{height:2px;width:38px;background:var(--gold)}
.footer-list{list-style:none;color:#e8e2d8;font-size:15px;line-height:29px}
.footer-list .current{color:var(--gold);text-decoration:underline}
.hours{color:#e8e2d8;font-size:15px;line-height:24px}
.hours span{display:inline-block;width:82px}
.thumb{width:95px;height:68px}
.footer-line{left:88px;top:3180px;width:1024px;height:1px;background:#4a4440}
.copyright{left:88px;top:3198px;color:#e8e2d8;font-size:13px;letter-spacing:.5px}
.copyright b{font-weight:400;color:var(--gold)}
.social{left:914px;top:3201px;display:flex;gap:20px}
.social span{width:12px;height:12px;border-radius:50%;background:#e8e2d8}
.social span.on{background:var(--gold)}
.to-top{left:1060px;top:3160px;width:52px;height:69px;background:#1f1d1b;display:flex;align-items:center;justify-content:center}
</style>
</head>
<body>

<header class="abs site-header">
  <nav>
    <a class="abs nav" style="left:503px"><span class="active">HOME</span></a>
    <a class="abs nav" style="left:595px">ABOUT US</a>
    <a class="abs nav" style="left:717px">MENU</a>
    <a class="abs nav" style="left:809px">CONTACT US</a>
  </nav>
  <a class="abs btn book-btn">BOOK NOW</a>
</header>
<div class="abs brand-box"><div class="brand-frame"><span class="brand-name">VELVET<br>KEY</span></div></div>

<section class="abs hero" role="img" aria-label="Dim speakeasy lounge with mustard tufted chairs, leather sofa and painted wall"></section>
<h1 class="abs hero-title">DELICIOUS FOODS<br>WITH WONDERFUL<br>EATING</h1>

<h2 class="abs section-title about-title">ABOUT US</h2>
<div class="abs title-rule about-rule"></div>
<div class="abs about-copy">
  <p>Lorem Ipsum is simply dummy text of the printing and typesetting industry.</p>
  <p>Lorem Ipsum has been the industry's standard dummy text ever since the 1500s, when an unknown printer took a galley of type and scrambled it to make a type specimen book. It has survived not only five centuries, but also the leap into electronic typesetting, remaining essentially unchanged...</p>
</div>
<a class="abs btn read-btn">READ MORE</a>
<div class="abs photo-chef" role="img" aria-label="Chef plating a dish in the kitchen"></div>
<div class="abs photo-wrap"></div>
<div class="abs photo-burrito" role="img" aria-label="Sliced burrito with beef, corn and herbs"></div>

<section class="abs menu-band" role="img" aria-label="Dark warm-toned food backdrop"></section>
<h2 class="abs section-title menu-title">OUR MENU</h2>
<div class="abs title-rule menu-rule"></div>
<div class="abs menu-card card-food" role="img" aria-label="Roast chicken dinner table with candles"></div>
<div class="abs menu-card card-drinks" role="img" aria-label="Back bar with bottles"><div class="drinks-mark">VELVET<br>KEY</div></div>
<div class="abs menu-card card-snacks" role="img" aria-label="Grilled club sandwiches on a plate"></div>
<div class="abs card-label" style="left:112px;top:1703px">LUNCH &amp; DINNER</div>
<div class="abs card-label" style="left:464px;top:1687px">DRINKS &amp; WINES</div>
<div class="abs card-label" style="left:816px;top:1703px">BITES &amp; SNACKS</div>

<div class="abs video-frame"></div>
<div class="abs video" role="img" aria-label="Video still of a chef cooking at the stove"></div>
<div class="abs play"><div class="play-inner">
  <svg width="24" height="26" viewBox="0 0 24 26"><path d="M4 3 L20 13 L4 23 Z" fill="none" stroke="#fff" stroke-width="2"/></svg>
</div></div>

<h2 class="abs section-title locate-title">LOCATE US</h2>
<div class="abs title-rule locate-rule"></div>
<div class="abs map" role="img" aria-label="Street map of the New York and New Jersey area"></div>

<div class="abs contact-item" style="top:2534px">
  <div class="contact-icon"><svg width="22" height="22" viewBox="0 0 24 24"><path d="M5 3h4l2 5-3 2a11 11 0 0 0 6 6l2-3 5 2v4a2 2 0 0 1-2 2A18 18 0 0 1 3 5a2 2 0 0 1 2-2z" fill="none" stroke="#fff" stroke-width="1.4"/></svg></div>
  <div class="contact-text"><div class="contact-label">PHONE</div><div class="contact-value">+1-201-555-0148</div></div>
</div>
<div class="abs contact-item" style="top:2626px">
  <div class="contact-icon"><svg width="22" height="18" viewBox="0 0 24 18"><rect x="1" y="1" width="22" height="16" fill="none" stroke="#fff" stroke-width="1.4"/><path d="M1 1l11 9 11-9" fill="none" stroke="#fff" stroke-width="1.4"/></svg></div>
  <div class="contact-text"><div class="contact-label">EMAIL</div><div class="contact-value">info@velvetkey.com</div></div>
</div>
<div class="abs contact-item" style="top:2717px">
  <div class="contact-icon"><svg width="18" height="24" viewBox="0 0 18 24"><path d="M9 23s8-9 8-14A8 8 0 0 0 1 9c0 5 8 14 8 14z" fill="none" stroke="#fff" stroke-width="1.4"/><circle cx="9" cy="9" r="3" fill="none" stroke="#fff" stroke-width="1.4"/></svg></div>
  <div class="contact-text"><div class="contact-label">ADDRESS</div><div class="contact-value">New Jersey, USA</div></div>
</div>

<footer class="abs site-footer"></footer>
<div class="abs footer-brand">VELVET<br>KEY</div>
<h3 class="abs footer-head" style="left:300px;top:2970px">QUICK LINKS</h3>
<div class="abs footer-rule" style="left:300px;top:2997px"></div>
<ul class="abs footer-list" style="left:301px;top:3012px">
  <li class="current">Home</li><li>About Us</li><li>Menu</li><li>Contact Us</li>
</ul>
<h3 class="abs footer-head" style="left:516px;top:2970px">HOURS</h3>
<div class="abs footer-rule" style="left:516px;top:2997px"></div>
<div class="abs hours" style="left:517px;top:3014px"><div><span>Sunday:</span>11am - 10pm</div><div><span>Mon-Sat:</span>11am - 10pm</div></div>
<div class="abs thumb" style="left:806px;top:2977px;background:linear-gradient(135deg,#e9d2a0,#b86a30)" role="img" aria-label="Club sandwich"></div>
<div class="abs thumb" style="left:911px;top:2977px;background:linear-gradient(135deg,#3a2a22,#8a4a30)" role="img" aria-label="Grilled meat platter"></div>
<div class="abs thumb" style="left:1016px;top:2977px;background:linear-gradient(135deg,#c04030,#7a9a40,#e0d8c0)" role="img" aria-label="Burrito"></div>
<div class="abs thumb" style="left:806px;top:3058px;background:#5a4a36;border:2px solid var(--gold)" role="img" aria-label="Dining room"></div>
<div class="abs thumb" style="left:911px;top:3058px;background:linear-gradient(135deg,#1a1a1a,#d0ccc6)" role="img" aria-label="Chef at work"></div>
<div class="abs thumb" style="left:1016px;top:3058px;background:linear-gradient(135deg,#6a4a30,#d89a40)" role="img" aria-label="Fried appetizers"></div>
<div class="abs footer-line"></div>
<p class="abs copyright">© 2023 <b>VELVET KEY</b>. All Right Reserved.</p>
<div class="abs social"><span></span><span class="on"></span><span></span><span></span></div>
<div class="abs to-top"><svg width="14" height="14" viewBox="0 0 14 14"><path d="M2 7l5-5 5 5M2 12l5-5 5 5" fill="none" stroke="#c79a4a" stroke-width="1.5"/></svg></div>

</body>
</html>
```